One page responsive Wordpress Website

I am looking to design and code for 1-page Wordpress responsive website (desktop/mobile/tablet). Pls see attached file. Job scope includes Wordpress design and coding of the actual Live website
Target Market(s)
Small medium business
Industry/Entity Type
Telecommunications
Font styles to use
Sans Serif
Colors
ffffff
85cae6
63bae0
33a6d7
cedeed
3277b5
Requirements
Must have
- One page only, Wordpress, Responsive layout in desktop, mobile, tablet

```html
<!DOCTYPE html>
<html lang="en">
<head>
<meta charset="utf-8">
<title>Velcora IP Phone</title>
<link rel="stylesheet" href="https://fonts.googleapis.com/css2?family=Lato:wght@400;700&family=Montserrat:wght@400;500;600;700;800&display=swap">
<style>
:root{
  --white:#ffffff;
  --sky-light:#85cae6;
  --sky:#63bae0;
  --azure:#33a6d7;
  --mist:#cedeed;
  --royal:#3277b5;
  --brand:#17a0e3;
  --navy:#1f4a8e;
  --ink:#1d1d1d;
  --text:#4a4a4a;
}
*{box-sizing:border-box;margin:0;padding:0}
html,body{width:1200px;height:2260px;overflow:hidden;background:var(--white)}
body{position:relative;font-family:"Lato",sans-serif;color:var(--ink)}

/* header */
.site-header{position:absolute;left:0;top:0;width:1200px;height:77px;background:var(--white)}
.brand-name{font-family:"Montserrat",sans-serif;font-weight:700;color:var(--brand);letter-spacing:0;font-style:normal}
.site-header .brand-name{position:absolute;left:117px;top:20px;font-size:32px;line-height:1}
.main-nav a{position:absolute;top:31px;font-family:"Montserrat",sans-serif;font-size:13px;color:var(--ink);text-decoration:none}

/* hero */
.hero{position:absolute;left:0;top:77px;width:1200px;height:705px}
.hero-bg{position:absolute;left:0;top:0}
.hero-sub{position:absolute;top:60px;width:1200px;text-align:center;font-family:"Montserrat",sans-serif;font-weight:400;font-size:26px;color:var(--white)}
.hero-title{position:absolute;top:96px;width:1200px;text-align:center;font-family:"Montserrat",sans-serif;font-weight:800;font-size:52px;color:var(--white);letter-spacing:0.5px}
.hero-lead{position:absolute;top:162px;width:1200px;text-align:center;font-size:17px;line-height:26px;color:var(--white)}
.product{position:absolute;top:252px;width:220px;text-align:center}
.product-photo{display:block;margin:0 auto;width:160px;height:222px;border-radius:6px;background:linear-gradient(160deg,#4a5563,#2b333d)}
.product-name{margin-top:40px;font-family:"Montserrat",sans-serif;font-weight:700;font-size:16px;color:var(--white)}
.btn-sheet{display:block;margin:14px auto 0;width:202px;height:40px;line-height:36px;border:2px solid var(--white);border-radius:22px;font-family:"Lato",sans-serif;font-weight:700;font-size:12.5px;color:var(--white);text-decoration:none}
.btn-sheet.is-solid{background:var(--white);color:var(--ink)}

/* about */
.about-photo{position:absolute;left:138px;top:866px;width:404px;height:404px;border-radius:50%;background:radial-gradient(circle at 45% 40%,#9aa6b0,#3c444d 70%,#e9e9e9 100%)}
.about-ring{position:absolute;left:128px;top:856px;width:428px;height:428px;border-radius:50%;border:2px solid var(--azure);clip-path:inset(0 40% 0 0)}
.section-title{font-family:"Montserrat",sans-serif;font-weight:700;color:var(--royal)}
.about-title{position:absolute;left:608px;top:906px;font-size:40px}
.about-rule{position:absolute;left:611px;top:961px;width:72px;height:3px;background:var(--royal)}
.about-text{position:absolute;left:611px;top:991px;font-size:17.5px;line-height:30.4px;color:var(--text);white-space:nowrap}

/* contact */
.contact{position:absolute;left:0;top:1377px;width:1200px;height:581px;overflow:hidden}
.contact-photo{position:absolute;left:0;top:0;width:700px;height:581px;background:linear-gradient(135deg,#2e5fb3 0%,#3a8ad0 55%,#4fa6dc 100%)}
.contact-panel{position:absolute;left:0;top:0}
.contact-title{position:absolute;left:142px;top:144px;font-family:"Montserrat",sans-serif;font-weight:400;font-size:35px;color:var(--white)}
.contact-title strong{font-weight:800}
.contact-rule{position:absolute;left:146px;top:197px;width:74px;height:3px;background:var(--white)}
.contact-intro{position:absolute;left:143px;top:231px;font-size:14px;font-weight:700;color:var(--white)}
.contact-text{position:absolute;left:144px;top:258px;width:380px;font-size:15.5px;line-height:24.5px;color:var(--white)}
.btn-touch{position:absolute;left:146px;top:360px;width:180px;height:41px;line-height:41px;text-align:center;background:var(--navy);font-family:"Montserrat",sans-serif;font-weight:700;font-size:12px;color:var(--white);text-decoration:none}
.form-title{position:absolute;left:641px;top:117px;font-family:"Montserrat",sans-serif;font-weight:400;font-size:20px;color:var(--white)}
.field{position:absolute;left:646px;width:456px;height:45px;background:var(--white);border:1px solid var(--mist);padding:0 22px;font-family:"Montserrat",sans-serif;font-size:13px;color:#8a8a8a;line-height:43px}
.field.is-message{height:87px;line-height:1;padding-top:16px}
.btn-send{position:absolute;left:649px;top:438px;width:181px;height:41px;border:2px solid var(--white);text-align:center;line-height:37px;font-family:"Montserrat",sans-serif;font-weight:700;font-size:13px;color:var(--white)}

/* footer */
.site-footer .brand-name{position:absolute;left:145px;top:2026px;font-size:36px;line-height:1}
.footer-about{position:absolute;left:156px;top:2080px;font-size:11.5px;line-height:19.5px;color:var(--text)}
.footer-copy{position:absolute;left:156px;top:2138px;font-family:"Montserrat",sans-serif;font-size:11.5px;line-height:21px;color:var(--text)}
.footer-heading{position:absolute;top:2027px;font-family:"Montserrat",sans-serif;font-weight:700;font-size:15.5px;color:var(--brand)}
.footer-links a{position:absolute;left:524px;font-size:13.5px;color:var(--ink);text-decoration:none}
.footer-contact li{position:absolute;left:742px;list-style:none;font-size:13px;color:var(--ink);display:flex;align-items:center;gap:13px}
.footer-contact svg{width:17px;height:17px;flex:none}
</style>
</head>
<body>

<header class="site-header">
  <span class="brand-name">Velcora</span>
  <nav class="main-nav">
    <a href="#about" style="left:824px">ABOUT US</a>
    <a href="#contact" style="left:972px">CONTACT US</a>
  </nav>
</header>

<section class="hero">
  <svg class="hero-bg" width="1200" height="705" viewBox="0 0 1200 705" role="img" aria-label="Blue abstract network background">
    <defs>
      <linearGradient id="heroGrad" x1="0" y1="0" x2="1" y2="1">
        <stop offset="0" stop-color="#2a86d4"/>
        <stop offset="0.45" stop-color="#4db3e6"/>
        <stop offset="1" stop-color="#1c6dc0"/>
      </linearGradient>
    </defs>
    <path d="M0 0H1200V629Q600 745 0 629Z" fill="url(#heroGrad)"/>
    <path d="M30 656Q600 760 1170 636" fill="none" stroke="#2d8fd0" stroke-width="3"/>
  </svg>
  <p class="hero-sub">Enterprise HD IP Phone</p>
  <h1 class="hero-title">VELCORA IP PHONE</h1>
  <p class="hero-lead">The most affordable IP Phone, with highest compatibility to every IP-PBX system.<br>Sleek designed and user-friendly proven.</p>

  <div class="product" style="left:162px">
    <span class="product-photo" role="img" aria-label="VC310 desk IP phone"></span>
    <h3 class="product-name">VELCORA VC310</h3>
    <a class="btn-sheet" href="#">Download datasheet (EN)</a>
  </div>
  <div class="product" style="left:500px">
    <span class="product-photo" role="img" aria-label="VC520 desk IP phone"></span>
    <h3 class="product-name">VELCORA VC520</h3>
    <a class="btn-sheet is-solid" href="#">Download datasheet (EN)</a>
  </div>
  <div class="product" style="left:826px">
    <span class="product-photo" role="img" aria-label="VX40 expansion module" style="width:116px;height:195px;margin-top:10px;background:linear-gradient(160deg,#2b3a55,#1a2438)"></span>
    <h3 class="product-name" style="margin-top:57px">VELCORA VX40</h3>
    <a class="btn-sheet" href="#" style="margin-top:11px">Download datasheet (EN)</a>
  </div>
</section>

<section id="about">
  <div class="about-ring"></div>
  <div class="about-photo" role="img" aria-label="Row of desk IP phones in an office"></div>
  <h2 class="section-title about-title">ABOUT US</h2>
  <div class="about-rule"></div>
  <p class="about-text">Velcora IP Phones is designed with pixel colour LCD with back-<br>light LED, built in Gigabit Ethernet with up to 28 various features<br>Equipped with Power over Ethernet ( support, and high defini-<br>tion ( sound quality with a rich visual experience Designed with<br>a fresh appearance, it supports flexible and secured provision-<br>ing, deliver modern elegant appearance, superb sound quality<br>and a rich set of IP/SIP telephony features</p>
</section>

<section class="contact" id="contact">
  <div class="contact-photo" role="img" aria-label="Customer support agent with headset at a desk, blue tint"></div>
  <svg class="contact-panel" width="1200" height="581" viewBox="0 0 1200 581">
    <defs>
      <linearGradient id="panelGrad" x1="0" y1="0" x2="1" y2="1">
        <stop offset="0" stop-color="#1f72c4"/>
        <stop offset="0.5" stop-color="#2f9fd6"/>
        <stop offset="1" stop-color="#33a6d7"/>
      </linearGradient>
    </defs>
    <path d="M649 0H1200V581H649Q560 450 575 300Q590 120 649 0Z" fill="url(#panelGrad)"/>
  </svg>
  <h2 class="contact-title"><strong>CONTACT</strong> US NOW</h2>
  <div class="contact-rule"></div>
  <p class="contact-intro">Speak to us or send us an enquiry for free consultation.</p>
  <p class="contact-text">Our team would love to share more about Velcora IP Phones. We are expecting your calls and emails. Drop us an enquiry form at your fingertips!</p>
  <a class="btn-touch" href="#">GET IN TOUCH</a>

  <h3 class="form-title">WRITE US WE’D LOVE TO HEAR FROM YOU!</h3>
  <div class="field" style="top:162px">Your Name *</div>
  <div class="field" style="top:219px">Phone *</div>
  <div class="field" style="top:277px">Email address*</div>
  <div class="field is-message" style="top:332px">Message</div>
  <div class="btn-send">SEND MESSAGE</div>
</section>

<footer class="site-footer">
  <span class="brand-name">Velcora</span>
  <p class="footer-about">Velcora IP Phones is designed with pixel colour LCD<br>with backlight LED, built in Gigabit Ethernet</p>
  <p class="footer-copy">© &nbsp;2020-2021 Velcora<br>All rights reserved. Terms of Use</p>

  <h4 class="footer-heading" style="left:524px">COMPANY</h4>
  <nav class="footer-links">
    <a href="#" style="top:2073px">Home</a>
    <a href="#about" style="top:2101px">About Us</a>
    <a href="#" style="top:2129px">News</a>
    <a href="#contact" style="top:2157px">Contact Us</a>
  </nav>

  <h4 class="footer-heading" style="left:739px">CONTACT US</h4>
  <ul class="footer-contact">
    <li style="top:2070px"><svg viewBox="0 0 16 16"><path d="M8 1a5 5 0 0 0-5 5c0 4 5 9 5 9s5-5 5-9a5 5 0 0 0-5-5zm0 7a2 2 0 1 1 0-4 2 2 0 0 1 0 4z" fill="#3277b5"/></svg>48 Harbourfront Lane, #07-12, Singapore 108822</li>
    <li style="top:2098px"><svg viewBox="0 0 16 16"><path d="M4 1l2.5 3-1.5 2c1 2 3 4 5 5l2-1.5 3 2.5-1.5 2.5C8 14 2 8 1.5 2.5z" fill="#3277b5"/></svg>6310-4477</li>
    <li style="top:2126px"><svg viewBox="0 0 16 16"><rect x="1.5" y="3.5" width="13" height="9" fill="none" stroke="#3277b5" stroke-width="1.3"/><path d="M1.5 3.5 8 9l6.5-5.5" fill="none" stroke="#3277b5" stroke-width="1.3"/></svg>hello@lumivox-systems.sg</li>
    <li style="top:2154px"><svg viewBox="0 0 16 16"><rect x="1" y="1" width="14" height="14" rx="1.5" fill="#3277b5"/></svg>Lumivox Business Systems Pte Ltd</li>
  </ul>
</footer>

</body>
</html>
```